Corvane Systems Modern, Sleek One Pager/Slick Sheet

Creative Brief: One-Pager Design for Corvane Systems
Project Overview:
We are seeking a highly skilled graphic designer to create a modern, sleek, and visually impactful one-pager (slick sheet) for Corvane Systems, a leading company in the defense and aerospace sector. This slick sheet will serve as a high-level marketing asset, designed to quickly capture attention and communicate Corvane Systems’s cutting-edge capabilities, technological expertise, and commitment to national security and innovation.
Key Objectives:
Establish a high-tech, sophisticated look and feel that aligns with the defense and aerospace industries.
Highlight Corvane Systems’s core competencies, key services, and differentiators with clear and concise messaging.
Ensure the design supports easy readability and quick scanning of critical information.
Incorporate strong visual hierarchy and premium, professional aesthetics.
Design Specifications:
Format: Single-page, print and digital distribution-ready (PDF format).
Layout Style: Clean, minimalist, and balanced with ample white space.
Typography: Modern, sans-serif fonts that convey innovation and strength.
Color Palette: Incorporate Corvane Systems’s brand colors (navy blue, steel gray, white, accents of metallic or deep reds if applicable).
Imagery: Use high-resolution imagery that reflects advanced technology, aerospace engineering, and national defense. Subtle technical graphics, schematics, or abstract patterns are acceptable to enhance visual interest without clutter.
Content Elements (To Be Provided):
Company Logo and Tagline
Key Capabilities and Service Offerings
Differentiators and Core Competencies
Contact Information
Visual Icons or Infographics for Quick Reference (if applicable)
Tone & Mood:
Professional, authoritative, and cutting-edge
Emphasizes trust, innovation, and mission-critical solutions
Appeals to government and defense industry stakeholders
Deliverables:
Final high-resolution print-ready PDF
Digital-friendly PDF optimized for email and web use
Source files (Adobe Illustrator, InDesign, or equivalent)
Target Market(s)
Defense/Aviation
Industry/Entity Type
Defense/Aviation
Look and feel

```html
<!DOCTYPE html>
<html lang="en">
<head>
<meta charset="utf-8">
<title>Corvane Systems – Aviation Services</title>
<link href="https://fonts.googleapis.com/css2?family=Montserrat:wght@400;500;600;800;900&display=swap" rel="stylesheet">
<style>
  :root{
    --navy:#24397b;
    --red:#a30f12;
    --ink:#1d1d1f;
    --white:#ffffff;
  }
  *{margin:0;padding:0;box-sizing:border-box;}
  html,body{width:719px;height:1200px;overflow:hidden;background:var(--white);}
  body{font-family:"Montserrat",sans-serif;color:var(--ink);}
  .sheet{position:relative;width:719px;height:1200px;overflow:hidden;background:var(--white);}

  .masthead{position:absolute;left:0;top:0;width:719px;height:132px;display:flex;align-items:center;justify-content:center;}
  .brand-name{font-size:34px;font-weight:500;letter-spacing:5px;color:#222;text-transform:uppercase;}

  .hero{position:absolute;left:0;top:132px;width:719px;height:356px;
    background:radial-gradient(ellipse at 50% 45%,#5fb7f0 0%,#2a78c4 30%,#153f86 62%,#0b1f4a 100%);}

  .band{position:absolute;left:0;top:488px;width:719px;height:76px;background:var(--navy);}
  .title-block{position:absolute;left:0;top:488px;width:358px;height:179px;background:var(--navy);}
  .title-block .kicker{position:absolute;left:43px;top:46px;font-size:35px;font-weight:800;color:var(--white);letter-spacing:.5px;line-height:1;}
  .title-block .headline{position:absolute;left:39px;top:86px;font-size:53px;font-weight:900;color:var(--white);line-height:1;letter-spacing:.5px;}

  .side-panel{position:absolute;left:358px;top:564px;width:361px;height:560px;
    background:linear-gradient(180deg,#ffffff 0%,#dfe8f4 30%,#c3d3e8 62%,#9ea4aa 78%,#8a8c8e 100%);}
  .side-foot{position:absolute;left:358px;top:1124px;width:361px;height:76px;background:var(--navy);}

  .service{position:absolute;display:flex;gap:10px;z-index:2;}
  .service .icon{flex:0 0 auto;width:60px;height:60px;border-radius:50%;background:var(--navy);display:flex;align-items:center;justify-content:center;}
  .service .icon svg{width:35px;height:35px;}
  .service h3{font-size:19px;font-weight:800;color:var(--red);line-height:1.08;text-transform:uppercase;margin-bottom:4px;white-space:nowrap;}
  .service p{font-size:11.6px;font-weight:500;line-height:1.42;color:var(--ink);white-space:nowrap;letter-spacing:-.15px;}

  .contact{position:absolute;left:42px;top:1128px;z-index:2;}
  .contact .line{display:flex;align-items:center;gap:8px;line-height:1.25;white-space:nowrap;}
  .contact svg{width:16px;height:16px;flex:0 0 auto;}
  .contact .phone{font-size:22px;font-weight:800;color:#111;}
  .contact .email{font-size:20px;font-weight:500;color:var(--navy);}
</style>
</head>
<body>
<main class="sheet">
  <header class="masthead">
    <span class="brand-name">Corvane Systems</span>
  </header>

  <div class="hero" role="img" aria-label="Photo of a jet airliner on a wet runway overlaid with glowing blue digital schematic lines"></div>

  <div class="band"></div>
  <div class="title-block">
    <div class="kicker">AVIATION</div>
    <h1 class="headline">SERVICES :</h1>
  </div>

  <div class="side-panel" role="img" aria-label="Photo of a white twin-turboprop aircraft parked on an airfield apron under a pale sky"></div>
  <div class="side-foot"></div>

  <section class="service" style="left:42px;top:708px;">
    <div class="icon"><svg viewBox="0 0 36 36" fill="none" stroke="#fff" stroke-width="2" stroke-linejoin="round"><path d="M26 6c-6 1-11 6-14 13l5 5c7-3 12-8 13-14z"/><circle cx="22" cy="14" r="2.5"/><path d="M12 19l-5 1 3-5 5-1M17 24l-1 5 5-3 1-5M10 26l-3 3"/></svg></div>
    <div>
      <h3>ISR Special Mission:</h3>
      <p>Global Intelligence, Surveillance, and<br>Reconnaissance providing creative<br>solutions in multi-domain operations</p>
    </div>
  </section>

  <section class="service" style="left:42px;top:821px;">
    <div class="icon"><svg viewBox="0 0 36 36" fill="none" stroke="#fff" stroke-width="2"><circle cx="13" cy="15" r="5"/><circle cx="13" cy="15" r="8" stroke-dasharray="3 2.5"/><circle cx="22" cy="21" r="5"/><path d="M26 25l6 6"/><path d="M26 5v3M21 7l2 2M31 7l-2 2"/></svg></div>
    <div>
      <h3>Research and<br>Development:</h3>
      <p>Specialize in testing of new technogies<br>for future ISR construct, next-generation<br>warfighting capabilities</p>
    </div>
  </section>

  <section class="service" style="left:42px;top:958px;">
    <div class="icon"><svg viewBox="0 0 36 36" fill="none" stroke="#fff" stroke-width="2" stroke-linecap="round"><circle cx="24" cy="13" r="6"/><circle cx="13" cy="9" r="2.5"/><path d="M13 12l-2 8 5 4-1 6M11 20l-4 7M13 14l5 2"/><path d="M5 31h26"/></svg></div>
    <div>
      <h3>CONUS Efforts:</h3>
      <p>State/Federal Low Enforcement,<br>Natural Disaster, search and Rescue,<br>Specialized SOF Programs</p>
    </div>
  </section>

  <section class="service" style="left:375px;top:607px;">
    <div class="icon"><svg viewBox="0 0 36 36" fill="none" stroke="#fff" stroke-width="2"><circle cx="18" cy="18" r="13" stroke-dasharray="4 2"/><circle cx="18" cy="18" r="8"/><path d="M14 22v-7M18 22v-9M22 22v-7"/></svg></div>
    <div>
      <h3>OCONUS Efforts:</h3>
      <p>Streamlining international collabora-<br>tion to shape the global landscape and<br>safeguarding our nation and allies</p>
    </div>
  </section>

  <section class="service" style="left:375px;top:713px;">
    <div class="icon"><svg viewBox="0 0 36 36" fill="none" stroke="#fff" stroke-width="2" stroke-linejoin="round"><path d="M13 5h18v14H22l-4 4v-4h-5z"/><path d="M17 10h10M17 14h7"/><circle cx="9" cy="19" r="3"/><path d="M4 31c0-5 2-7 5-7s5 2 5 7"/></svg></div>
    <div>
      <h3>Aviation Training:</h3>
      <p>Solving complex problems with<br>dynamic solutions for future<br>warfighters</p>
    </div>
  </section>

  <footer class="contact">
    <div class="line phone">
      <svg viewBox="0 0 24 24" fill="#111"><path d="M6.6 10.8c1.4 2.8 3.8 5.2 6.6 6.6l2.2-2.2c.3-.3.7-.4 1-.2 1.1.4 2.3.6 3.6.6.6 0 1 .4 1 1V20c0 .6-.4 1-1 1C10.6 21 3 13.4 3 4c0-.6.4-1 1-1h3.5c.6 0 1 .4 1 1 0 1.3.2 2.5.6 3.6.1.3 0 .7-.2 1z"/></svg>
      <span>CALL: (555) 014-2290</span>
    </div>
    <div class="line email">
      <svg viewBox="0 0 24 24" fill="#111"><path d="M2 5h20v14H2z"/><path d="M2 5l10 8 10-8" fill="none" stroke="#fff" stroke-width="1.8"/></svg>
      <span>info@corvanesystems.com</span>
    </div>
  </footer>
</main>
</body>
</html>
```